Quarrow financial services, is a financial company that provides consultancy, brokerage services, and funding.

we will be providing the clients with insights, knowledge and data with regards to the financial markets.

with the brokerage services we will try to find the suitable counterparts that provide them with the best investments that suits their needs and expected return.

Target Market(s)

financial institutions, Corporates, high-net worth individuals

Industry/Entity Type

Financial Service

Contact Information for Business Card

Font styles to use
Other font styles liked:
• applemyungjo

Colors
00a990
848484

Requirements
Must have
• the logo at the back
Nice to have
• Finesse
Should not have
• boldness

```html
<!DOCTYPE html>
<html lang="en">
<head>
<meta charset="utf-8">
<title>Quarrow Financial Services – Business Card</title>
<link href="https://fonts.googleapis.com/css2?family=Open+Sans:wght@400;600&display=swap" rel="stylesheet">
<style>
  :root {
    --page-bg: #3b3b3b;
    --card-white: #ffffff;
    --sage: #d7e2c7;
    --mist: #c8cbcd;
    --leaf-green: #7b9a48;
    --slate: #3f4a52;
    --ink: #555a5e;
  }
  html, body {
    margin: 0;
    padding: 0;
    width: 1105px;
    height: 1200px;
    overflow: hidden;
    background: var(--page-bg);
  }
  .canvas {
    position: relative;
    width: 1105px;
    height: 1200px;
  }
  .card {
    position: absolute;
    left: 196px;
    width: 720px;
    height: 412px;
    background: var(--card-white);
    overflow: hidden;
    box-shadow: 0 3px 8px rgba(0,0,0,0.45);
  }
  .card--front { top: 146px; }
  .card--back  { top: 602px; }

  /* Front */
  .block { position: absolute; }
  .block--sage {
    left: 0; top: 0;
    width: 369px; height: 278px;
    background: var(--sage);
  }
  .block--mist {
    left: 351px; top: 133px;
    width: 369px; height: 279px;
    background: var(--mist);
  }
  .front-mark {
    position: absolute;
    left: 300px; top: 184px;
    width: 120px;
    text-align: center;
    font-family: "Open Sans", sans-serif;
    font-size: 20px;
    font-weight: 400;
    line-height: 1.2;
    color: var(--slate);
  }
  .contact {
    position: absolute;
    left: 41px; top: 38px;
    font-family: "Open Sans", sans-serif;
    color: var(--ink);
  }
  .contact__name {
    margin: 0;
    font-size: 25px;
    font-weight: 600;
    color: var(--leaf-green);
    line-height: 1.2;
  }
  .contact__role {
    margin: 2px 0 10px;
    font-size: 19px;
    line-height: 1.2;
  }
  .contact__line {
    display: flex;
    align-items: center;
    gap: 12px;
    font-size: 18.5px;
    line-height: 29px;
  }
  .contact__line svg {
    width: 17px;
    height: 17px;
    fill: var(--leaf-green);
    flex: none;
  }
  .address {
    position: absolute;
    right: 37px; top: 278px;
    text-align: right;
    font-family: "Open Sans", sans-serif;
    font-style: normal;
    font-size: 18.5px;
    line-height: 25px;
    color: var(--ink);
  }
  .address__web {
    margin-top: 2px;
    font-weight: 600;
    color: var(--slate);
  }

  /* Back */
  .brand {
    position: absolute;
    left: 0; right: 0; top: 92px;
    display: flex;
    flex-direction: column;
    align-items: center;
  }
  .brand__square {
    width: 56px;
    height: 100px;
    background: var(--mist);
    margin-bottom: 34px;
  }
  .brand__name {
    font-family: "Open Sans", sans-serif;
    font-size: 30px;
    font-weight: 400;
    line-height: 1.2;
    color: var(--slate);
  }
</style>
</head>
<body>
<div class="canvas">

  <section class="card card--front">
    <div class="block block--sage"></div>
    <div class="block block--mist"></div>
    <div class="front-mark">Quarrow</div>

    <div class="contact">
      <h1 class="contact__name">MARA ELLISON</h1>
      <p class="contact__role">CEO/Founder</p>
      <div class="contact__line">
        <svg viewBox="0 0 24 24" aria-hidden="true"><path d="M6.6 10.8a15.1 15.1 0 0 0 6.6 6.6l2.2-2.2c.3-.3.7-.4 1-.2 1.1.4 2.3.6 3.6.6.6 0 1 .4 1 1V20c0 .6-.4 1-1 1A17 17 0 0 1 3 4c0-.6.4-1 1-1h3.5c.6 0 1 .4 1 1 0 1.3.2 2.5.6 3.6.1.3 0 .7-.2 1z"/></svg>
        <span>555 214 7036</span>
      </div>
      <div class="contact__line">
        <svg viewBox="0 0 24 24" aria-hidden="true"><path d="M2 5h20v2l-10 7L2 7z"/><path d="M2 9l10 7 10-7v10H2z"/></svg>
        <span>mara@quarrowfs.com</span>
      </div>
    </div>

    <address class="address">
      <div>412 Alder Court</div>
      <div>Brookhaven</div>
      <div>Alaska 34120</div>
      <div class="address__web">www.quarrowfs.com</div>
    </address>
  </section>

  <section class="card card--back">
    <div class="brand">
      <div class="brand__square"></div>
      <div class="brand__name">Quarrow Financial Services</div>
    </div>
  </section>

</div>
</body>
</html>
```